Velmora Skincare packaging designs

We are need to create packaging for our skincare brand. We need two designs. One for round jars which is for creams/capsules and the second will be for bottles/serums Some products will be larger in size so please ensure the packaging design will work and there isn't a lot white/empty space

Below are the names of some of our products.
Screw-On Top Jar (25 pads- 4 inches wide) - Glint Wipes I Skin Brightening Pads
Pump Bottle (2 oz) - ReKINDLE I Hyaluronic Acid + Vitamin Serum
Pump Bottle (6oz) - The Cloud Rinse I Conditioning Face Cleanser
Dropper bottle (1 oz) - Sunny Veil I Hydrating Moisturizer
Cream jar (1.5 oz) - Sunny Veil I Hydrating Moisturizer
Capsules Jar (25 capsules in a jar)- Lumo Burst I Moisture + Hydrating Capsules
Capsules Jar (25 capsules in a jar) - Pure Spark I Impurity Capsules

We will also need help with the packing design in terms of layout of the logo, item name, desc, and ingredients on each product.

Target Market(s)

women

Industry/Entity Type

skincare, beauty

Font styles to use
Sans Serif

Colors
E54698
E96AAD
F1A4CE
F9D9EA
FCEFF6

Requirements
Must have
• Pantone color is 2052 CP HEX #DAAFCA (218 , 175 , 202)

```html
<!DOCTYPE html>
<html lang="en">
<head>
<meta charset="UTF-8">
<title>Velmora Skincare – Glint Wipes jar label</title>
<link rel="stylesheet" href="https://fonts.googleapis.com/css2?family=Nunito+Sans:wght@300;400;700;800&display=swap">
<style>
  :root {
    --bg: #e3e3e3;
    --lid: #141414;
    --lid-soft: #2a2a2a;
    --rose: #c9698f;
    --rose-deep: #b04a6c;
    --rose-line: #e6a3bf;
    --body-top: #dab0ca;
    --body-bottom: #c592b3;
    --white: #ffffff;
    --paper: #f2f2f2;
  }
  * { margin: 0; padding: 0; box-sizing: border-box; }
  html, body { width: 872px; height: 1200px; overflow: hidden; }
  body {
    background: var(--bg);
    font-family: "Nunito Sans", sans-serif;
    position: relative;
  }

  /* Lid side band */
  .lid-band {
    position: absolute;
    left: 205px; top: 116px;
    width: 451px; height: 104px;
    background: linear-gradient(180deg, var(--lid) 0%, var(--lid-soft) 50%, var(--lid) 100%);
    border-radius: 6px 6px 2px 2px;
    overflow: hidden;
  }
  .lid-band__wordmark {
    position: absolute;
    left: -8px; top: 50px;
    white-space: nowrap;
    color: var(--rose-line);
    font-weight: 700;
    font-size: 14px;
    letter-spacing: 0.3px;
    word-spacing: 6px;
  }
  .lid-band__rule {
    position: absolute;
    left: 0; right: 0; top: 80px;
    height: 2px;
    background: var(--rose-line);
  }

  /* Jar label */
  .label {
    position: absolute;
    left: 205px; top: 220px;
    width: 451px; height: 256px;
    background: linear-gradient(180deg, var(--body-top) 0%, var(--body-top) 60%, var(--body-bottom) 100%);
    border-radius: 0 0 14px 14px;
  }
  .label__brand-box {
    position: absolute;
    left: 36px; top: 37px;
    width: 136px; height: 164px;
    background: var(--paper);
    border: 2px solid var(--rose);
    display: flex; align-items: center; justify-content: center;
  }
  .label__brand {
    color: var(--rose);
    font-weight: 700;
    font-size: 20px;
    letter-spacing: 2px;
  }
  .label__copy {
    position: absolute;
    left: 202px; top: 42px;
    width: 220px;
    color: var(--white);
  }
  .label__name {
    font-weight: 800;
    font-size: 31px;
    line-height: 1;
    letter-spacing: -0.5px;
    white-space: nowrap;
  }
  .label__subtitle {
    margin-top: 10px;
    display: inline-block;
    font-size: 12.5px;
    font-weight: 400;
    letter-spacing: 3px;
    padding-bottom: 3px;
    border-bottom: 1px solid var(--white);
    white-space: nowrap;
  }
  .label__desc {
    margin-top: 12px;
    font-size: 11px;
    font-weight: 300;
    line-height: 14.5px;
  }
  .label__volume {
    display: inline-block;
    margin-top: 14px;
    padding: 2px 9px;
    font-size: 10.5px;
    font-weight: 400;
    border-radius: 10px;
    background: linear-gradient(90deg, var(--rose-deep), #d98aa8);
  }

  /* Lid top */
  .lid-top {
    position: absolute;
    left: 211px; top: 660px;
    width: 450px; height: 450px;
  }
</style>
</head>
<body>

  <div class="lid-band">
    <div class="lid-band__wordmark">VELMORA VELMORA VELMORA VELMORA VELMORA VELMORA VELMORA VELMORA</div>
    <div class="lid-band__rule"></div>
  </div>

  <section class="label">
    <div class="label__brand-box">
      <span class="label__brand">VELMORA</span>
    </div>
    <div class="label__copy">
      <h1 class="label__name">GLINT WIPES</h1>
      <p class="label__subtitle">SKIN BRIGHTENING PADS</p>
      <p class="label__desc">Advanced Probiotic Recovery Complex<br>Scientifically Formulated for sensitive<br>&amp; Reactive Skin</p>
      <span class="label__volume">1.7 FL.OZ. / ℮ 50ml</span>
    </div>
  </section>

  <svg class="lid-top" viewBox="0 0 450 450" aria-label="Lid top">
    <circle cx="225" cy="225" r="224" fill="var(--lid)"/>
    <circle cx="225" cy="225" r="205" fill="none" stroke="var(--rose)" stroke-width="2.5"/>
    <text x="225" y="238" text-anchor="middle" fill="var(--rose)"
          font-family="Nunito Sans, sans-serif" font-weight="700" font-size="40" letter-spacing="4">VELMORA</text>
  </svg>

</body>
</html>
```